FREE BBQ for life if you win our business with your creative menu design

Looking for a 11x17 size menu. we are a full service BBQ restaurant. We have an upscale environment as well as up scale service. We offer 5 star dinning at a casual price. we are on route 66 and are proud of that. we offer the finest smoked meats. Specializing in smoked pork beef and bison. we have an old barn wood decor. we only use oak to smoke our meats. use a lot of tarnished metal as well as some string nail art. Looking for a menu that goes along our style. i have attached as many pictures as i could to give you a fill of how we do it out here.
PLEASE USE THE 11"X17" MENU TEMPLATE ATTACHED IN THE PROJECT BRIEF.
Target Market(s)
Cool people and there families.
Industry/Entity Type
Business
Requirements
Must have
- I have attached the Current menu we use. File pollards menu pub. Those are all the Items. There will be some changes as we but together the new menu. The prices are changing. but that should be an easy change as we go.
Nice to have
- We are getting away from the lunch dinner menu and going to an all day menu. so rather than coming with toast or bun we will now be asking as an option. I have attached a menu i tried to make as a sample of how we will be doing it. new menu single page and new menu single page flame. These are ideas i had but could not really make it work. so use them as an idea of what we are looking for but be creative.

```html
<!DOCTYPE html>
<html lang="en">
<head>
<meta charset="utf-8">
<title>Pollards Barbeque Menu</title>
<link href="https://fonts.googleapis.com/css2?family=Rokkitt:wght@400;600;700&family=Arimo:wght@400;700&display=swap" rel="stylesheet">
<style>
:root{
  --backdrop:#3b3a39;
  --wood-dark:#4e2812;
  --wood:#7a4421;
  --wood-light:#a1602f;
  --parchment:#f3e6c8;
  --parchment-edge:#e2a24a;
  --burn:#c8461a;
  --ink:#1d1410;
  --ink-soft:#3e322a;
  --price:#d62a1e;
  --cream:#f4e7cf;
  --sauce:#5a1d0c;
  --bean:#8a3d1c;
  --app-blue:#39a9e0;
}
*{margin:0;padding:0;box-sizing:border-box}
html,body{width:1200px;height:828px;overflow:hidden;background:var(--backdrop)}
body{position:relative;font-family:"Arimo",Arial,sans-serif;color:var(--ink)}
.page{position:absolute;top:54px;width:478px;height:736px;overflow:hidden;
  background:repeating-linear-gradient(90deg,var(--wood) 0 38px,var(--wood-dark) 38px 40px,var(--wood-light) 40px 76px,var(--wood-dark) 76px 78px);}
.page--cover{left:96px}
.page--menu{left:622px}

/* cover */
.brand-card{position:absolute;left:22px;top:52px;width:230px;height:206px;
  background:linear-gradient(160deg,#d9a25d,#c27a33 60%,#e8932a);
  transform:rotate(-4deg);box-shadow:0 4px 10px rgba(0,0,0,.5);text-align:center;padding-top:48px}
.brand-card__pin{position:absolute;right:34px;top:-6px;width:16px;height:16px;border-radius:50%;background:var(--price)}
.brand-card__name{font-family:"Rokkitt",serif;font-weight:700;font-size:35px;line-height:.95;color:var(--ink);text-transform:uppercase}
.brand-card__phone{font-family:"Rokkitt",serif;font-weight:700;font-size:17px;margin-top:12px;color:var(--ink)}
.cover-title{position:absolute;left:260px;top:124px;width:196px;text-align:center;font-family:"Rokkitt",serif;font-weight:700;font-size:66px;color:var(--cream);line-height:1}
.cover-phone{position:absolute;left:260px;top:190px;width:196px;text-align:center;font-family:"Rokkitt",serif;font-size:18px;color:var(--cream);letter-spacing:1px}
.cover-photo{position:absolute;left:0;top:274px;width:478px;height:462px;
  background:radial-gradient(ellipse at 30% 40%,var(--bean),transparent 40%),radial-gradient(ellipse at 65% 45%,var(--sauce),#2a0e05 70%);
  clip-path:polygon(0 6%,8% 3%,16% 7%,25% 2%,36% 5%,48% 1%,60% 6%,72% 2%,84% 5%,94% 1%,100% 4%,100% 100%,0 100%)}
.route-badge{position:absolute;left:46px;top:614px;width:74px;height:78px}
.loyalty{position:absolute;left:240px;top:702px;font-family:"Rokkitt",serif;font-size:7.6px;line-height:1.3;color:var(--cream);display:flex;gap:6px;align-items:center}
.loyalty__app{font-family:"Rokkitt",serif;font-weight:700;font-size:16px;color:var(--app-blue)}

/* inside page */
.parchment{position:absolute;left:18px;top:34px;width:448px;height:656px;background:var(--parchment);
  box-shadow:inset 0 0 14px 6px var(--parchment-edge),inset 0 0 3px 2px var(--burn);
  clip-path:polygon(0 2%,6% 0,18% 1.5%,32% 0,48% 1%,62% 0,78% 1.2%,92% 0,100% 1%,99% 20%,100% 45%,99% 70%,100% 98%,88% 100%,70% 98.8%,52% 100%,34% 99%,16% 100%,0 99%,1% 70%,0 40%,1% 18%)}
.menu-brand{position:absolute;left:48px;top:72px;font-family:"Rokkitt",serif;line-height:1}
.menu-brand__name{font-size:17px;font-weight:600}
.menu-brand__word{font-size:32px;font-weight:700}
.plate-photo{position:absolute;left:18px;top:142px;width:220px;height:112px;border-radius:50%;
  background:radial-gradient(ellipse at 60% 45%,#c98a3a,#8a5a2a 45%,#eee 62%,#d8d8d8 70%)}
.section{position:absolute;width:172px}
.section--left{left:48px}
.section--right{left:254px}
.section__title{display:flex;align-items:center;height:26px;white-space:nowrap;font-family:"Rokkitt",serif;font-weight:600;font-size:26px;line-height:1;margin-bottom:6px}
.section__tag{font-size:6.6px;font-weight:700;font-family:"Arimo",Arial,sans-serif;margin-left:5px}
.tag-dot{display:inline-block;width:11px;height:11px;border-radius:50%;background:#2f5aa6;margin-left:12px}
.mascot{display:inline-block;width:22px;height:32px;border-radius:10px;background:linear-gradient(#f1d9b0,#d63b2a);margin-left:8px}
.item{margin-bottom:1.5px}
.item__name{font-weight:700;font-size:8px;line-height:1.15}
.item__name--small{font-size:7px}
.price{color:var(--price)}
.price--small{font-size:5.6px}
.item__desc{font-size:5.2px;line-height:1.22;color:var(--ink-soft)}
.note{font-size:6.4px;color:var(--price);line-height:1.3;margin-top:5px}
.note + .note{margin-top:3px}
.sides-list{display:grid;grid-template-columns:116px 1fr;font-size:6.4px;font-weight:700;line-height:1.3}
.soda-marks{position:absolute;right:0;top:30px;display:flex;flex-direction:column;gap:8px}
.soda-marks span{display:block;width:28px;height:10px;background:#1c4fa0}
.soda-marks span+span{background:#8c1a2a}
</style>
</head>
<body>

<section class="page page--cover">
  <div class="brand-card">
    <span class="brand-card__pin"></span>
    <div class="brand-card__name">Pollards<br>Barbeque</div>
    <div class="brand-card__phone">505-555-0142</div>
  </div>
  <h1 class="cover-title">MENU</h1>
  <div class="cover-phone">505-555-0142</div>
  <div class="cover-photo" role="img" aria-label="Photo of glazed smoked ribs with a bowl of baked beans and grilled Texas toast"></div>
  <svg class="route-badge" viewBox="0 0 74 80" aria-hidden="true">
    <path d="M6 10 Q37 -2 68 10 L66 40 Q62 66 37 78 Q12 66 8 40 Z" fill="#f1ede4" stroke="#2a2a2a" stroke-width="3"/>
  </svg>
  <div class="loyalty"><span class="loyalty__app">Tabi</span><span>Join our Customer loyalty app.<br>Get free food when you become a loyal customer.</span></div>
</section>

<section class="page page--menu">
  <div class="parchment"></div>

  <div class="menu-brand">
    <div class="menu-brand__name">Pollards</div>
    <div class="menu-brand__word">BARBEQUE</div>
  </div>
  <div class="plate-photo" role="img" aria-label="Photo of a plate with smothered Texas toast and fried okra"></div>

  <div class="section section--right" style="top:92px">
    <h2 class="section__title">APPETIZERS</h2>
    <div class="item"><div class="item__name">King Rings - <span class="price">7.89</span></div><div class="item__desc">Green Chili battered fried golden crispy 1" thick onion rings. Served with spicy ranch.</div></div>
    <div class="item"><div class="item__name">Deep Fried Pickles - <span class="price">7.89</span></div><div class="item__desc">Crisp dill pickle chips battered and fried to a golden crispy brown. Served with spicy ranch.</div></div>
    <div class="item"><div class="item__name">Fried Okra - <span class="price">7.89</span></div><div class="item__desc">Okra is breaded then fried until golden. Served with spicy ranch.</div></div>
    <div class="item"><div class="item__name">Green Chili Waffle Fries - <span class="price">7.89</span></div><div class="item__desc">Crispy waffle-cut Fries, topped with a savory blend of cheese, and New Mexico green chile. Served with spicy ranch.</div></div>
    <div class="item"><div class="item__name">KC Wild Wings - <span class="price">9.99</span></div><div class="item__desc">Big, meaty pork wings, deep fried to a perfect golden brown, tossed in a hot Buffalo-style sauce, and served with spicy buttermilk ranch dressing on the side. Served with spicy ranch.</div></div>
    <div class="item"><div class="item__name">Sampler Platter - <span class="price">8.99</span></div><div class="item__desc">Two KC Wild Wings, 6oz of Fried Pickles, 6oz of King Rings. Served with spicy ranch.</div></div>
  </div>

  <div class="section section--left" style="top:277px">
    <h2 class="section__title">BISON<span class="mascot" role="img" aria-label="Heart healthy mascot illustration"></span><span class="section__tag">Heart Healthy</span></h2>
    <div class="item"><div class="item__name">Bison Brisket - <span class="price">18.65</span></div><div class="item__desc">The belly of beast, smoked then sliced thin and grilled. Juicy and tender</div></div>
    <div class="item"><div class="item__name">Bison Burger - <span class="price">12.59</span></div><div class="item__desc">Smoked then grilled served with pepper jack cheese lettuce tomato pickle toped with spicy ranch.</div></div>
    <div class="item"><div class="item__name">Bison Steak - <span class="price">34.56</span></div><div class="item__desc">12oz of lean healthy meat cooked to your desired temp.</div></div>
    <div class="note">* Served with 1 sides and your choice of Texas toast, Kaiser bun, or Glutton Free bread</div>
  </div>

  <div class="section section--left" style="top:420px">
    <h2 class="section__title">SMOKED<span class="tag-dot"></span><span class="section__tag">Glutton free</span></h2>
    <div class="item"><div class="item__name">Baby Back Ribs - <span class="price price--small">Full Rack 22.59 - Half Rack 12.49</span></div><div class="item__desc">Tender to the bone, finger licking good, never need a knife, best ribs you'll ever have.</div></div>
    <div class="item"><div class="item__name">St. Louis Ribs - <span class="price price--small">Half 16.45 - Full 30.89</span></div><div class="item__desc">A nice big tender rib, slow smoked, so tender that you can sink your teeth into.</div></div>
    <div class="item"><div class="item__name">Beef Brisket - <span class="price">10.95</span></div><div class="item__desc">The most insane mouth watering smoky, moist, succulent piece of meat your mouth will ever have.</div></div>
    <div class="item"><div class="item__name">Pulled Pork - <span class="price">9.59</span></div><div class="item__desc">Smoked for 18-20 hrs. then pulled and mixed with our signature base barbeque sauce.</div></div>
    <div class="item"><div class="item__name">Sliced Pork - <span class="price">10.54</span></div><div class="item__desc">Smoked juicy tenderloin sliced thin then grilled per order.</div></div>
    <div class="item"><div class="item__name">Smoked Turkey - <span class="price">11.49</span></div><div class="item__desc">Breast meat smoked and sliced. Juicy and tender.</div></div>
    <div class="item"><div class="item__name">Smoked Chicken half - <span class="price">13.59</span></div><div class="item__desc">Moist and juicy smoked Breast and thigh on the bone basted with our signature sauce on the grill.</div></div>
    <div class="item"><div class="item__name">Rib Eye - <span class="price">21.95</span></div><div class="item__desc">12oz. juicy steak grilled to your desired temp</div></div>
    <div class="note">*Served with 1 sides and your choice of Texas toast, Kaiser bun, or Glutton Free bread</div>
    <div class="note">**All meats are Glutton free Please specify if you are glutton Intolerant.</div>
  </div>

  <div class="section section--right" style="top:280px">
    <h2 class="section__title">SALADS</h2>
    <div class="item"><div class="item__name">All you can eat salad bar - <span class="price">7.89</span></div><div class="item__desc">Enjoy as much salad as you would like</div></div>
    <div class="item"><div class="item__name">Meaty Salad - <span class="price">3.00</span></div><div class="item__desc">Choose any meat to add to your salad 3oz of meat. (Excludes ribs and bison.)</div></div>
    <div class="item"><div class="item__name item__name--small">Side Salad - With out meal <span class="price">3.00</span> - Add to meal <span class="price">1.50</span></div></div>
  </div>

  <div class="section section--right" style="top:380px">
    <h2 class="section__title">SIDES</h2>
    <div class="sides-list">
      <span>*Green Chile Creamed Corn</span><span>*Baked Beans</span>
      <span>*Potato Salad</span><span>*Waffle Fries</span>
      <span>*Baked Potato</span><span>*Coleslaw</span>
      <span>*Grilled Veggies</span><span class="price">**Extra side 2.29</span>
    </div>
  </div>

  <div class="section section--right" style="top:466px">
    <h2 class="section__title">DESSERTS</h2>
    <div class="item"><div class="item__name">Peach Cobbler &amp; Ice Cream - <span class="price price--small">large 5.89 Small 3.29</span></div><div class="item__desc">Served hot topped with ice cream.</div></div>
    <div class="item"><div class="item__name">Cookies A-L-Mode - <span class="price price--small">large 5.89 Small 3.29</span></div><div class="item__desc">Hot gooey cookies topped with ice cream your choice chocolate chip or macadamia nut. large 5.89 Small</div></div>
    <div class="item"><div class="item__name item__name--small">* Dessert of the week</div><div class="item__desc">Ask your server for our special dessert of the week</div></div>
  </div>

  <div class="section section--right" style="top:562px">
    <h2 class="section__title">DRINKS</h2>
    <div class="soda-marks" aria-hidden="true"><span></span><span></span></div>
    <div class="item"><div class="item__name">Lemonade - <span class="price">2.59</span></div><div class="item__desc">Regular, Strawberry, Watermelon, Cherry, Peach</div></div>
    <div class="item"><div class="item__name">Fountain - <span class="price">1.89</span></div><div class="item__desc">Cola, Pepper Soda, Root Beer, Lemon-Lime, Citrus Dew,<br>Diet Cola, Diet Pepper Soda</div></div>
    <div class="item"><div class="item__name">Iced Teas - <span class="price">1.89</span></div></div>
    <div class="item"><div class="item__name">Coffee - <span class="price">2.69</span></div></div>
    <div class="item"><div class="item__name">Hot Chocolate - <span class="price">2.89</span></div></div>
  </div>

  <div class="loyalty"><span class="loyalty__app">Tabi</span><span>Join our Customer loyalty app.<br>Get free food when you become a loyal customer.</span></div>
</section>

</body>
</html>
```